High-End Medical Center Website Design Project

This design is part of a well thought-out project by an experienced project manager / developer. The approved wireframe is attached. Creative interpretations / suggestions based on the layout encouraged.

The design is for a new state-of-the-art medical center located in Dallas, Texas. The target audience would likely be individuals (approx. 60% female /40% male) who are the healthcare decision-makers for their families. They would likely have insurance and be inclined to seek out top-quality care.

Potential clients would choose this client over others in their industry because the medical center is physician owned, meaning it is patient-focused rather than profit-focused. The facility is brand new, featuring the latest technology. (This includes an amazing waiting room featuring WiFi and docking stations.) The physicians are hand-picked by referral only.

The look of the site should be extremely clean. We are going for a well-organized, professional look with a bit of a warm glow (interpret that however you like). Use crisp corners and the colors in the logo.

Think modern, clean with some great use of color / font.

We can get lovely photography of the medical center once construction is complete. Feel free to use an "example image" behind the Featured Area ("Physician Owned. Patient-Focused") if you like. We are open to ideas.

ONE CHANGE REQUESTED IN THE WIREFRAME:

Remove the "Connect" 1/4 page footer area and replace with a quick contact form. You may swap the "Locations" area with the form if desired. Put social media icons at the top left of the page in the top header area.

(Note: Please use social media icons that match the design rather than standard icons. We preferred not placing the icons at the top, but the client requested this. Let's not bring more attention to them than necessary.)
Updates

We're custom programming this site, so there's no need to base it on a template. Also, we would prefer not to use typical "seen everywhere" stock images.Thanks.

Industry/Entity Type

Construction

Requirements
Must have
• Follow the wireframe. This has been approved.
Nice to have
• Examples of what hover states, links or dropdowns might look like.

```html
<!DOCTYPE html>
<html lang="en">
<head>
<meta charset="utf-8">
<title>Nova Medical Center</title>
<link href="https://fonts.googleapis.com/css2?family=Lato:wght@300;400;700;900&family=Roboto+Condensed:wght@400&family=Arimo:ital,wght@0,400;0,700;1,400&display=swap" rel="stylesheet">
<style>
:root{
  --blue:#0b57a8;
  --navy:#0b3d78;
  --teal:#5db6c6;
  --footer:#3b6d9e;
  --footer-bar:#1f4f85;
  --ink:#1c4f86;
  --grey:#6b6b6b;
  --white:#ffffff;
  --field:#f1f1ea;
}
*{margin:0;padding:0;box-sizing:border-box}
html,body{width:985px;height:1200px;overflow:hidden;background:#fff}
body{position:relative;font-family:"Arimo",Arial,sans-serif;color:var(--grey)}
.abs{position:absolute}
a{color:inherit;text-decoration:none}
.cond{font-family:"Roboto Condensed","Arial Narrow",sans-serif}

/* hero */
.hero{left:0;top:0;width:985px;height:690px;
  background:linear-gradient(100deg,#c9d5df 0%,#e9eef3 28%,#b7c9d8 45%,#d8e6ef 62%,#9fb9cf 78%,#e4ecf2 100%)}
.header{left:0;top:0;width:985px;height:72px;background:linear-gradient(90deg,rgba(60,150,190,.85),rgba(93,182,198,.9))}
.logo-block{left:142px;top:0;width:164px;height:72px;background:var(--blue)}
.logo{left:148px;top:18px;height:40px;display:flex;align-items:center;gap:8px;font-family:"Lato",sans-serif;font-weight:900;font-size:22px;color:var(--white);letter-spacing:.5px;white-space:nowrap}
.logo i{display:block;width:13px;height:13px;background:var(--white)}
.phone{left:668px;top:10px;display:flex;align-items:center;gap:8px;font-family:"Lato",sans-serif;font-size:21px;font-weight:700;color:var(--navy);white-space:nowrap}
.nav a{position:absolute;top:38px;height:34px;line-height:34px;font-size:12.5px;color:var(--white);letter-spacing:.4px;text-transform:uppercase;white-space:nowrap;text-align:center}
.nav a.active{background:var(--blue)}
.nav a.active::after{content:"";position:absolute;left:50%;bottom:-7px;margin-left:-7px;border:7px solid transparent;border-bottom:0;border-top-color:var(--blue)}
.nav a:hover{color:#dff3ff}
.hero-title{left:0;width:985px;text-align:center;font-family:"Lato",sans-serif;color:var(--white);text-shadow:0 2px 6px rgba(0,0,0,.25);white-space:nowrap}
.t1{top:190px;font-weight:300;font-size:46px;letter-spacing:1px}
.t2{top:234px;font-weight:700;font-size:52px;letter-spacing:1px}
.btn{background:var(--blue);color:var(--white);text-transform:uppercase;letter-spacing:.6px;border-radius:14px;text-align:center;display:block;white-space:nowrap}
.btn:hover{background:var(--navy)}
.appt{left:408px;top:312px;width:152px;height:27px;line-height:27px;font-size:12.5px}

/* features */
.apart-tab{left:358px;top:377px;width:254px;height:35px}
.apart-label{left:358px;top:385px;width:254px;text-align:center;font-family:"Lato",sans-serif;font-weight:700;font-size:15px;color:var(--white);white-space:nowrap}
.features{left:0;top:412px;width:985px;height:266px;background:rgba(255,255,255,.82);border-bottom:6px solid rgba(200,214,226,.8)}
.feature{top:418px;width:250px;text-align:center}
.feature .icon{width:125px;height:125px;border-radius:50%;background:var(--blue);margin:0 auto;display:flex;align-items:center;justify-content:center}
.feature h3{margin-top:18px;font-family:"Lato",sans-serif;font-weight:700;font-size:19px;color:var(--navy);letter-spacing:.3px;white-space:nowrap}
.feature p{margin:6px auto 0;width:200px;font-size:9px;line-height:13.4px;color:var(--ink)}
.divider{top:412px;width:1px;height:266px;background:rgba(180,195,210,.6)}

/* content */
.portrait{left:142px;top:732px;width:158px;height:220px;border:4px solid #e8e8e8;background:linear-gradient(180deg,#f4f4f4,#dfe6ec 55%,#c7d1db)}
.heading{left:320px;top:736px;font-family:"Lato",sans-serif;font-size:20px;font-weight:700;color:var(--navy)}
.body-copy{left:320px;top:768px;width:266px;font-size:9.8px;line-height:15.4px}
.body-copy p+p{margin-top:3px}
.more{width:84px;height:21px;line-height:21px;font-size:12px}
.testimonials{left:589px;top:724px;width:247px;height:246px;border:3px solid #e8e8e8}
.testimonials h2{position:absolute;left:18px;top:10px;font-family:"Lato",sans-serif;font-size:20px;font-weight:700;color:var(--navy)}
.quote{position:absolute;left:20px;width:212px}
.avatar{position:absolute;left:0;top:0;width:36px;height:36px;border:2px solid #ddd;background:linear-gradient(180deg,#dcdcdc,#9a9a9a)}
.quote p{margin-left:43px;font-size:10px;line-height:16px;color:var(--blue)}
.quote p b{color:#bbb;font-family:"Lato",sans-serif;font-size:14px}
.quote cite{display:block;text-align:right;font-size:9.5px;color:var(--grey);margin-top:2px}
.sep{position:absolute;left:20px;top:120px;width:160px;height:1px;background:#ddd}

/* footer */
.footer{left:0;top:986px;width:985px;height:172px;background:var(--footer)}
.col h4{font-family:"Lato",sans-serif;font-weight:400;font-size:14px;color:var(--white);letter-spacing:.2px;white-space:nowrap}
.col{color:#e8f0f7;font-size:8.5px;line-height:11px}
.news-row{display:flex;gap:8px;margin-top:12px}
.date{flex:0 0 28px;height:30px;background:var(--white);color:var(--navy);text-align:center;font-size:14px;font-weight:700;line-height:16px;margin-top:2px}
.date small{display:block;font-size:7px;line-height:9px}
.pill{display:inline-block;background:var(--white);color:var(--navy);font-size:8px;padding:1px 4px;margin-right:3px}
.count{display:inline-block;background:#e9eef3;color:#555;font-size:8px;padding:1px 3px;margin-right:14px}
.blog-item{margin-bottom:8px}
.blog-item em{display:block;text-align:right;color:var(--white);font-size:8.5px;margin-top:2px}
.wait{width:135px;height:32px;background:#1a73c9;color:var(--white);font-family:"Lato",sans-serif;font-size:19px;text-align:center;line-height:32px;letter-spacing:1px}
.loc a{display:inline-block;width:72px;text-decoration:underline;color:var(--white);margin-right:5px;vertical-align:top}
.field{width:171px;height:21px;background:linear-gradient(180deg,#fbfbf6,var(--field));border:1px solid #d0d0c6;font-size:9px;color:#333;padding:5px 10px}
.submit{width:68px;height:20px;line-height:20px;font-size:12px;background:var(--navy)}
.bar{left:0;top:1158px;width:985px;height:42px;background:var(--footer-bar);color:var(--white);font-size:9.5px}
.social{left:428px;top:1167px;display:flex;gap:4px}
.social span{width:22px;height:22px;border-radius:50%;background:var(--white)}
.bar-links{left:559px;top:1173px;display:flex;white-space:nowrap}
.bar-links a{padding:0 7px;border-right:1px solid rgba(255,255,255,.6);line-height:11px}
.bar-links a:first-child{padding-left:0}
.bar-links a:last-child{border:0}
.bar-links a:hover{text-decoration:underline}
</style>
</head>
<body>

<div class="abs hero" role="img" aria-label="Photo of a smiling physician in a white coat with colleagues in a bright clinic corridor behind him"></div>

<header>
  <div class="abs header"></div>
  <div class="abs logo-block"></div>
  <div class="abs logo"><i></i>NOVA MEDICAL</div>
  <div class="abs phone">
    <svg width="18" height="18" viewBox="0 0 24 24"><path fill="#0b3d78" d="M6.6 10.8a15.1 15.1 0 0 0 6.6 6.6l2.2-2.2a1 1 0 0 1 1-.25 11.4 11.4 0 0 0 3.6.57 1 1 0 0 1 1 1V20a1 1 0 0 1-1 1A17 17 0 0 1 3 4a1 1 0 0 1 1-1h3.5a1 1 0 0 1 1 1c0 1.25.2 2.45.57 3.57a1 1 0 0 1-.25 1z"/></svg>
    (555) 010-2040
  </div>
  <nav class="nav cond">
    <a href="#" class="active" style="left:424px;width:80px">Why Nova</a>
    <a href="#" style="left:512px;width:60px">Physians</a>
    <a href="#" style="left:588px;width:66px">Specialist</a>
    <a href="#" style="left:668px;width:42px">Info</a>
    <a href="#" style="left:720px;width:62px">Locations</a>
    <a href="#" style="left:796px;width:52px">Contact</a>
  </nav>
</header>

<div class="abs hero-title t1">PHYSICIAN OWNED</div>
<div class="abs hero-title t2">PATIENT FOCUSED</div>
<a href="#" class="abs btn appt cond">Make an Appointment</a>

<section>
  <div class="abs features"></div>
  <svg class="abs apart-tab" viewBox="0 0 254 35"><polygon points="28,0 226,0 254,35 0,35" fill="#0b3d78"/></svg>
  <div class="abs apart-label">WHATS SETS US APART</div>
  <div class="abs divider" style="left:376px"></div>
  <div class="abs divider" style="left:594px"></div>

  <div class="abs feature" style="left:145px">
    <div class="icon">
      <svg width="76" height="76" viewBox="0 0 76 76" fill="none" stroke="#fff" stroke-width="4" stroke-linecap="round">
        <path d="M14 12c-6 10-4 22 8 26 10 3 18-4 20-14"/>
        <path d="M22 38c0 14 8 24 22 24s18-10 12-20"/>
        <circle cx="56" cy="38" r="6" fill="#fff"/>
      </svg>
    </div>
    <h3>TECHNOLOGY</h3>
    <p>Lorem ipsum dolor sit amet, consectetuer adipiscing elit, sed diam nonummy nibh euismod tincidunt ut laoreet dolore magna aliquam erat volutpat. Ut wisi enim ad minim veniam, quis nostrud exerci tation ullamcorper suscipit lobortis nisl ut aliquip ex ea commodo consequat.</p>
  </div>

  <div class="abs feature" style="left:360px">
    <div class="icon">
      <svg width="80" height="80" viewBox="0 0 80 80">
        <circle cx="40" cy="40" r="26" fill="none" stroke="#fff" stroke-width="4"/>
        <circle cx="40" cy="15" r="10" fill="#fff"/>
        <circle cx="18" cy="54" r="10" fill="#fff"/>
        <circle cx="62" cy="54" r="10" fill="#fff"/>
      </svg>
    </div>
    <h3>QUALITY OF CARE</h3>
    <p>Lorem ipsum dolor sit amet, consectetuer adipiscing elit, sed diam nonummy nibh euismod tincidunt ut laoreet dolore magna aliquam erat volutpat. Ut wisi enim ad minim veniam, quis nostrud exerci tation ullamcorper suscipit lobortis nisl ut aliquip ex ea commodo consequat.</p>
  </div>

  <div class="abs feature" style="left:587px">
    <div class="icon">
      <span style="font-family:'Lato',sans-serif;font-weight:900;font-size:76px;color:#fff;line-height:1">?</span>
    </div>
    <h3>PATIENT EXPERIENCE</h3>
    <p>Lorem ipsum dolor sit amet, consectetuer adipiscing elit, sed diam nonummy nibh euismod tincidunt ut laoreet dolore magna aliquam erat volutpat. Ut wisi enim ad minim veniam, quis nostrud exerci tation ullamcorper suscipit lobortis nisl ut aliquip ex ea commodo consequat.</p>
  </div>
</section>

<main>
  <div class="abs portrait" role="img" aria-label="Portrait photo of a young doctor in a white coat with a stethoscope, arms crossed"></div>
  <h2 class="abs heading">HEADING 1</h2>
  <div class="abs body-copy">
    <p>Lorem ipsum dolor sit amet, consectetuer adipiscing elit, sed diam nonummy nibh euismod tincidunt ut laoreet dolore magna aliquam erat volutpat. Ut wisi enim ad minim veniam, quis nostrud exerci tation ullamcorper suscipit lobortis nisl ut aliquip ex ea commodo consequat.</p>
    <p>Lorem ipsum dolor sit amet, consectetuer adipiscing elit, sed diam nonummy nibh euismod tincidunt ut laoreet dolore magna aliquam erat volutpat. Ut wisi enim ad minim veniam, quis nostrud exerci tation ullamcorper suscipit lobortis nisl ut aliquip ex ea commodo consequat.</p>
  </div>
  <a href="#" class="abs btn more cond" style="left:319px;top:937px">Read More</a>

  <aside class="abs testimonials">
    <h2>TESTIMONIALS</h2>
    <div class="quote" style="top:42px">
      <div class="avatar" role="img" aria-label="Customer headshot"></div>
      <p><b>&ldquo;</b> Lorem ipsum dolor sit amet, consectetuer adipiscing elit, sed diam nonummy nibh euismod tincidunt ut laoreet dolore <b>&rdquo;</b></p>
      <cite>Lena Marsh</cite>
    </div>
    <div class="sep"></div>
    <div class="quote" style="top:132px">
      <div class="avatar" role="img" aria-label="Customer headshot"></div>
      <p><b>&ldquo;</b> Lorem ipsum dolor sit amet, consectetuer adipiscing elit, sed diam nonummy nibh euismod tincidunt ut laoreet dolore <b>&rdquo;</b></p>
      <cite style="margin-top:8px">Paul Rivers</cite>
    </div>
    <a href="#" class="btn more cond" style="position:absolute;left:18px;top:209px">Read More</a>
  </aside>
</main>

<footer>
  <div class="abs footer"></div>

  <div class="abs col" style="left:142px;top:998px;width:160px">
    <h4>NEWS</h4>
    <div class="news-row">
      <div class="date">17<small>JAN</small></div>
      <p>Lorem ipsum dolor sit amet, consectetuer adipiscing elit, sed diam nonummy nibh euismod</p>
    </div>
    <p style="margin-top:3px">Lorem ipsum dolor sit amet, consectetuer adipiscing elit, se</p>
    <p style="margin-top:7px"><span class="pill">Like</span><span class="count">2.6k</span><span class="pill">Share</span><span class="count">13</span></p>
    <p style="margin-top:7px;font-weight:700;color:#fff">Readmore</p>
  </div>

  <div class="abs col" style="left:323px;top:998px;width:160px">
    <h4>BLOG</h4>
    <div class="blog-item" style="margin-top:11px">Lorem ipsum dolor sit amet, consectetuer adipiscing elit, sed diam nonummy nibh euismod<em>3 hours Ago</em></div>
    <div class="blog-item">Lorem ipsum dolor sit amet, consectetuer adipiscing elit, sed diam nonummy nibh euismod<em>3 hours Ago</em></div>
  </div>

  <div class="abs col" style="left:505px;top:998px;width:160px">
    <h4>AVERAGE WAIT TIME</h4>
    <div class="wait" style="margin-top:9px">00 : 09 : 00</div>
    <h4 style="margin-top:12px">LOCATIONS</h4>
    <p class="loc" style="margin-top:6px"><a href="#">Lorem ipsum sit amet, conse er adipiscing elit</a><a href="#" style="margin-right:0">Lorem ipsum sit amet, conse er adipiscing elit</a></p>
  </div>

  <form class="abs col" style="left:671px;top:998px;width:180px">
    <h4>REGISTER FOR FREE HERE!</h4>
    <p style="margin-top:9px">Lorem ipsum dolor sit amet, consectet.</p>
    <div class="field" style="margin-top:10px">Your Name</div>
    <div class="field" style="margin-top:7px">Your Email</div>
    <a href="#" class="btn submit cond" style="margin:8px 0 0 107px">Submit</a>
  </form>

  <div class="abs bar"></div>
  <div class="abs" style="left:144px;top:1172px;color:#fff;font-size:9.5px;white-space:nowrap">&copy; 2013 | Nova Medical Care All rights reserved</div>
  <div class="abs social" aria-label="Social links"><span></span><span></span><span></span><span></span></div>
  <nav class="abs bar-links" style="color:#fff;font-size:9.5px">
    <a href="#">Why Nova</a><a href="#">Physians</a><a href="#">Specialist</a><a href="#">Info</a><a href="#">Locations</a><a href="#">Contact</a>
  </nav>
</footer>

</body>
</html>
```